Kalmoret Windham & Associates

We would like a simple, professional business card using a similar font to our logo.

Industry/Entity Type

Law Firm

Contact Information for Business Card

Martin Kalmoret, Esq. 47 Tillman Lane, 2nd Floor Marshfield, MA 02050 Office: 781.555.0143 Cell: 508.555.0196 Email: marty@kwfirmma.com kalmoretwindhamlaw.com

Font styles to use
Other font styles liked:
• We would like to use the fonts used in the logo or similar

Colors
0054AA
0677BA
7BADD7
CADEEF
E8F1F8

Requirements
Must have
• We would like the fonts to match the logo
Nice to have
• not too much design- very simple and professional business card. I added a picture of a business card that I tried to start but I am not a designer! Hopefully it will help with the address and phone numbers and kind of what we are looking for.

```html
<!DOCTYPE html>
<html lang="en">
<head>
<meta charset="utf-8">
<title>Kalmoret Windham &amp; Associates – Business Card</title>
<link rel="stylesheet" href="https://fonts.googleapis.com/css2?family=Cinzel:wght@700&family=Lora:wght@400&display=swap">
<style>
  :root {
    --backdrop: #cacaca;
    --card-white: #ffffff;
    --brand-blue: #0229a0;
    --ink-grey: #4e5858;
    --rule-grey: #9aa0a0;
    --card-edge: #222222;
  }
  * { box-sizing: border-box; margin: 0; padding: 0; }
  html, body {
    width: 1200px; height: 846px; overflow: hidden;
    background: var(--backdrop);
  }
  .canvas { position: relative; width: 1200px; height: 846px; }

  .card { position: absolute; left: 345px; width: 508px; height: 290px; }
  .card--front { top: 113px; background: var(--card-white); border: 1px solid var(--card-edge); }
  .card--back { top: 444px; background: var(--brand-blue); }

  /* Front */
  .front-firm {
    position: absolute; left: 76px; top: 96px; width: 160px;
    font-family: "Lora", serif; font-weight: 400;
    color: var(--brand-blue); font-size: 24px; line-height: 1.2;
  }
  .holder-name {
    position: absolute; left: 252px; top: 82px;
    font-family: "Cinzel", serif; font-weight: 700;
    font-size: 18.5px; letter-spacing: 0.4px; color: var(--brand-blue);
  }
  .contact-list {
    position: absolute; left: 251px; top: 110px; list-style: none;
    font-family: "Lora", serif; font-size: 12.6px; color: var(--ink-grey);
  }
  .contact-list li { display: flex; align-items: center; height: 18.3px; }
  .contact-list svg { width: 12px; height: 12px; margin-right: 5px; flex: none; }
  .divider-rule {
    position: absolute; left: 78px; top: 215px; width: 348px; height: 1px;
    background: var(--rule-grey);
  }
  .address {
    position: absolute; left: 0; right: 0; top: 224px; text-align: center;
    font-family: "Lora", serif; font-size: 12.6px; letter-spacing: 0.2px; color: var(--ink-grey);
  }

  /* Back */
  .back-square {
    position: absolute; left: 72px; top: 102px; width: 157px; height: 86px;
    background: var(--card-white);
  }
  .back-divider {
    position: absolute; left: 244px; top: 86px; width: 2px; height: 118px;
    background: var(--card-white);
  }
  .back-firm {
    position: absolute; left: 260px; top: 106px;
    font-family: "Lora", serif; font-weight: 400;
    color: var(--card-white); font-size: 23px; line-height: 1.2;
  }
</style>
</head>
<body>
<main class="canvas">
  <section class="card card--front" aria-label="Business card front">
    <div class="front-firm">Kalmoret Windham</div>
    <h1 class="holder-name">MARTIN KALMORET</h1>
    <ul class="contact-list">
      <li>
        <svg viewBox="0 0 12 12" aria-hidden="true"><path d="M4 1.2c-1.6.7-2.2 2.7-1.6 5 .6 2.3 2 4 3.8 4.6l1-1.6-1.6-1.2-.8.5c-.7-.7-1.1-1.6-1.3-2.7l.9-.4L4.7 3 4 1.2z" fill="var(--ink-grey)"/></svg>
        office: 781.555.0143
      </li>
      <li>
        <svg viewBox="0 0 12 12" aria-hidden="true"><rect x="3.2" y="1" width="5.6" height="10" rx="1" fill="none" stroke="var(--ink-grey)" stroke-width="0.9"/><line x1="5.2" y1="9.6" x2="6.8" y2="9.6" stroke="var(--ink-grey)" stroke-width="0.8"/></svg>
        cell: 508.555.0196
      </li>
      <li>
        <svg viewBox="0 0 12 12" aria-hidden="true"><rect x="0.8" y="2.6" width="10.4" height="7" fill="var(--ink-grey)"/><path d="M0.8 2.6 6 6.8l5.2-4.2" fill="none" stroke="#fff" stroke-width="0.8"/></svg>
        marty@kwfirmma.com
      </li>
      <li>
        <svg viewBox="0 0 12 12" aria-hidden="true"><g fill="none" stroke="var(--ink-grey)" stroke-width="0.8"><circle cx="6" cy="6" r="5"/><ellipse cx="6" cy="6" rx="2.2" ry="5"/><line x1="1" y1="6" x2="11" y2="6"/><path d="M1.8 3.5h8.4M1.8 8.5h8.4"/></g></svg>
        kalmoretwindhamlaw.com
      </li>
    </ul>
    <div class="divider-rule"></div>
    <p class="address">Esq. 47 Tillman Lane, 2nd Floor Marshfield, MA 02050</p>
  </section>

  <section class="card card--back" aria-label="Business card back">
    <div class="back-square"></div>
    <div class="back-divider"></div>
    <div class="back-firm">Kalmoret<br>Windham<br>&amp; Associates</div>
  </section>
</main>
</body>
</html>
```